Vorbanix Stationery Design Project

We need a stationery design for our new business Vorbanix which deals in advanced cleaning technologies such as Ultrasonic cleaning and high pressure cleaning machinery.

Our colour scheme is as per the included files.

We require business cards, letterheads, a brochure folder and email signatures design
Updates

Project Deadline Extended

Apologies for the delay in making a decision on this project. We will be making a final decision during the course of next week

Target Market(s)

Industries ranging from medical, automotive, mining, engineering all requiring specialised cleaning services

Industry/Entity Type

Pressure Cleaning

Requirements
Must have
• Please include our supplied logo and colour scheme. The design needs to be professional but creative.

```html
<!DOCTYPE html>
<html lang="en">
<head>
<meta charset="utf-8">
<title>Vorbanix Stationery</title>
<link href="https://fonts.googleapis.com/css2?family=Open+Sans:wght@400;600;700&display=swap" rel="stylesheet">
<style>
  :root{
    --bg:#1c1c1f;
    --navy-deep:#080b33;
    --navy:#141d6b;
    --blue:#22339a;
    --silver:#c9cad2;
    --paper:#f4f4f6;
    --ink:#2b2f55;
    --grey:#6b6e80;
    --white:#ffffff;
  }
  *{margin:0;padding:0;box-sizing:border-box}
  html,body{width:1200px;height:1000px;overflow:hidden;background:var(--bg);font-family:"Open Sans",Arial,sans-serif}
  .sheet{position:absolute;overflow:hidden}
  .brand{display:flex;align-items:center;gap:6px}
  .brand-square{width:14px;height:14px;background:var(--blue)}
  .brand-name{font-weight:700;letter-spacing:1px;color:var(--ink);font-size:16px;line-height:1}
  .tagline{font-size:7px;color:var(--grey);margin-left:20px;margin-top:2px;white-space:nowrap}
  .on-dark .brand-square{background:var(--silver)}
  .on-dark .brand-name{color:var(--white)}
  .on-dark .tagline{color:#9ea3c8}
  .footer-band{position:absolute;left:0;right:0;bottom:0;background:linear-gradient(90deg,var(--navy),var(--blue));color:var(--white);font-size:4.5px;font-weight:600;padding:5px 8px;white-space:nowrap}
  .band-svg{position:absolute;left:0;width:100%}

  /* folder */
  .folder-front{left:40px;top:40px;width:330px;height:450px;background:linear-gradient(160deg,var(--navy) 0%,var(--navy-deep) 70%)}
  .folder-front .brand{position:absolute;right:28px;top:190px}
  .folder-front .brand-name{font-size:22px}
  .folder-front .brand-square{width:20px;height:20px}
  .folder-front .tagline{font-size:8px}
  .folder-back{left:390px;top:40px;width:330px;height:450px;background:linear-gradient(200deg,var(--navy) 0%,var(--navy-deep) 75%)}
  .folder-back .logo-small{position:absolute;left:50%;bottom:40px;transform:translateX(-50%)}
  .folder-back .brand-name{font-size:12px}
  .folder-back .brand-square{width:10px;height:10px}
  .folder-back .address{position:absolute;left:0;right:0;bottom:16px;text-align:center;font-size:5.5px;color:#9ea3c8}
  .folder-inside{left:740px;top:40px;width:420px;height:450px;background:linear-gradient(180deg,#d9d9de,#b7b8bf)}
  .letter{position:absolute;left:40px;top:30px;width:340px;height:390px;background:var(--paper);padding:22px 26px;font-size:7px;color:#444;line-height:1.6}
  .letter .brand{margin-bottom:2px}
  .letter .tagline{margin-bottom:18px}
  .letter p{margin-bottom:10px}
  .pocket{position:absolute;left:0;bottom:0;width:420px;height:150px}

  /* letterhead */
  .letterhead{left:40px;top:520px;width:310px;height:440px;background:var(--paper)}
  .letterhead .head{position:absolute;left:22px;top:22px}
  .letterhead .body-field{position:absolute;left:22px;right:22px;top:70px;bottom:40px;border-radius:6px;background:#ececf0}

  /* business cards */
  .card-front{left:370px;top:520px;width:230px;height:130px;background:var(--paper)}
  .card-front .brand{position:absolute;left:14px;top:76px}
  .card-front .brand-name{font-size:13px}
  .card-front .brand-square{width:11px;height:11px}
  .card-front .card-tagline{position:absolute;left:14px;top:92px;margin-left:17px;font-size:6px}
  .card-front .contact{position:absolute;left:124px;top:12px;font-size:6px;color:var(--ink);line-height:1.55}
  .card-front .contact b{font-size:7.5px}
  .card-back{left:370px;top:670px;width:230px;height:130px;background:linear-gradient(160deg,var(--navy),var(--navy-deep))}
  .card-back .brand{position:absolute;left:50%;top:50%;transform:translate(-50%,-50%)}
  .card-back .url{position:absolute;left:0;right:0;bottom:12px;text-align:center;font-size:6px;color:#9ea3c8}

  /* compliments slip */
  .compliments{left:620px;top:520px;width:320px;height:150px;background:var(--paper)}
  .compliments .brand{position:absolute;left:16px;top:18px}
  .compliments .tagline{position:absolute;left:16px;top:36px}
  .compliments .address{position:absolute;right:18px;top:14px;font-size:6px;color:var(--ink);line-height:1.5}
  .compliments .title-bar{position:absolute;right:0;bottom:0;width:210px;height:26px;background:var(--blue);color:var(--white);font-weight:700;font-size:12px;letter-spacing:.5px;display:flex;align-items:center;justify-content:flex-end;padding-right:12px}

  /* envelopes */
  .envelope-front{left:620px;top:690px;width:320px;height:170px;background:var(--paper)}
  .envelope-front .brand{position:absolute;left:16px;top:16px}
  .envelope-front .tagline{position:absolute;left:16px;top:34px}
  .envelope-back{left:960px;top:520px;width:200px;height:150px;background:var(--paper)}
  .envelope-back .flap{position:absolute;left:0;top:0;width:100%;height:40px}
  .envelope-back .brand{position:absolute;left:50%;top:12px;transform:translateX(-50%)}
  .envelope-back .brand-name{font-size:10px}
  .envelope-back .brand-square{width:9px;height:9px}
</style>
</head>
<body>

<!-- Folder front cover -->
<section class="sheet folder-front on-dark">
  <svg class="band-svg" style="top:0;height:450px" viewBox="0 0 330 450" preserveAspectRatio="none">
    <defs>
      <linearGradient id="swoosh" x1="0" y1="1" x2="1" y2="0">
        <stop offset="0" stop-color="#6f7080"/><stop offset=".5" stop-color="#e9e9ee"/><stop offset="1" stop-color="#9c9dab"/>
      </linearGradient>
    </defs>
    <path d="M120 450 Q230 360 330 300 L330 450 Z" fill="#1a2886"/>
    <path d="M100 450 Q220 350 330 285 L330 305 Q230 365 135 450 Z" fill="url(#swoosh)"/>
  </svg>
  <div class="brand"><span class="brand-square"></span><span class="brand-name">VORBANIX</span></div>
  <div class="tagline" style="position:absolute;right:28px;top:218px;margin:0">Advanced Cleaning Technologies</div>
</section>

<!-- Folder back cover -->
<section class="sheet folder-back on-dark">
  <div class="logo-small brand"><span class="brand-square"></span><span class="brand-name">VORBANIX</span></div>
  <div class="address">Address Goes Here, City, State, Zipcode • T +012-345-6789 • E info@vorbanix.com.au • www.vorbanix.com.au</div>
</section>

<!-- Folder inside with letter and pocket -->
<section class="sheet folder-inside">
  <article class="letter">
    <div class="brand"><span class="brand-square"></span><span class="brand-name">VORBANIX</span></div>
    <div class="tagline">Advanced Cleaning Technologies</div>
    <p>Jane Doe<br>Company Name<br>Street Address</p>
    <p>Dear Jane,</p>
    <p>Thank you for your interest in our cleaning services. Our ultrasonic and high pressure systems serve medical, automotive, mining and engineering clients. Please find our service details enclosed in this folder.</p>
    <p>Kind regards,<br><br>John Smith</p>
  </article>
  <svg class="pocket" viewBox="0 0 420 150" preserveAspectRatio="none">
    <path d="M0 150 L0 60 Q200 70 420 0 L420 150 Z" fill="#141d6b"/>
    <path d="M0 60 Q200 70 420 0 L420 8 Q200 78 0 68 Z" fill="#c9cad2"/>
  </svg>
</section>

<!-- Letterhead -->
<section class="sheet letterhead">
  <div class="head">
    <div class="brand"><span class="brand-square"></span><span class="brand-name">VORBANIX</span></div>
    <div class="tagline">Advanced Cleaning Technologies</div>
  </div>
  <div class="body-field"></div>
  <div class="footer-band">Address Goes Here, City, State, Zipcode • T +012-345-6789 • F +012-345-6789 • E info@vorbanix.com.au • www.vorbanix.com.au</div>
</section>

<!-- Business card front -->
<section class="sheet card-front">
  <div class="brand"><span class="brand-square"></span><span class="brand-name">VORBANIX</span></div>
  <div class="tagline card-tagline">Advanced Cleaning Technologies</div>
  <div class="contact">
    <b>John Smith</b><br>Managing Director<br><br>T +012-345-6789<br>E john@vorbanix.com.au<br>W www.vorbanix.com.au
  </div>
  <svg class="band-svg" style="bottom:0;height:16px" viewBox="0 0 230 16" preserveAspectRatio="none">
    <path d="M0 16 L0 6 Q120 10 230 0 L230 16 Z" fill="#22339a"/>
  </svg>
</section>

<!-- Business card back -->
<section class="sheet card-back on-dark">
  <div class="brand"><span class="brand-square"></span><span class="brand-name">VORBANIX</span></div>
  <div class="url">www.vorbanix.com.au</div>
</section>

<!-- Compliments slip -->
<section class="sheet compliments">
  <div class="brand"><span class="brand-square"></span><span class="brand-name">VORBANIX</span></div>
  <div class="tagline">Advanced Cleaning Technologies</div>
  <div class="address">Address Goes Here<br>City, State, Zipcode<br>T +012-345-6789<br>F +012-345-6789<br>E info@vorbanix.com.au<br>www.vorbanix.com.au</div>
  <svg class="band-svg" style="bottom:0;height:34px" viewBox="0 0 320 34" preserveAspectRatio="none">
    <path d="M0 34 L0 20 Q60 24 120 8 L120 34 Z" fill="#141d6b"/>
    <path d="M0 20 Q60 24 120 8 L126 8 Q62 28 0 25 Z" fill="#c9cad2"/>
  </svg>
  <div class="title-bar">WITH COMPLIMENTS</div>
</section>

<!-- Envelope front -->
<section class="sheet envelope-front">
  <div class="brand"><span class="brand-square"></span><span class="brand-name">VORBANIX</span></div>
  <div class="tagline">Advanced Cleaning Technologies</div>
  <svg class="band-svg" style="bottom:14px;height:16px" viewBox="0 0 320 16" preserveAspectRatio="none">
    <path d="M0 16 Q160 10 320 0 L320 16 Z" fill="#c9cad2"/>
  </svg>
  <div class="footer-band">Address Goes Here, City, State, Zipcode • T +012-345-6789 • F +012-345-6789 • E info@vorbanix.com.au • www.vorbanix.com.au</div>
</section>

<!-- Envelope back -->
<section class="sheet envelope-back on-dark">
  <svg class="flap" viewBox="0 0 200 40" preserveAspectRatio="none">
    <path d="M0 0 H200 V34 Q100 40 0 34 Z" fill="#141d6b"/>
  </svg>
  <div class="brand"><span class="brand-square"></span><span class="brand-name">VORBANIX</span></div>
</section>

</body>
</html>
```